Web Design For Staffing Company

We need a homepage web design for a technical staffing company.

Please see attached brief for project details.

please make the site modern with bold colors while matching the logo

Be sure to read the attached breif in full beforehand.

Target Market(s)

technical companies looking to hire talent

Industry/Entity Type

Staffing

Number of Pages Required

1 page

Font styles to use
Sans Serif

```html
<!DOCTYPE html>
<html lang="en">
<head>
<meta charset="utf-8">
<title>Northgate Talent – Technical Staffing</title>
<link href="https://fonts.googleapis.com/css2?family=Roboto+Condensed:ital,wght@0,400;0,700;1,700&family=Roboto:ital,wght@0,400;0,500;0,700;1,400&display=swap" rel="stylesheet">
<style>
:root{
  --navy:#0b2f55;
  --navy-deep:#071f3a;
  --blue:#1762a8;
  --blue-bright:#2a7fd0;
  --sky:#9fd2ff;
  --ink:#2c2c2c;
  --muted:#6b6b6b;
  --line:#d9d9d9;
  --paper:#ffffff;
  --mist:#eceef1;
}
*{box-sizing:border-box;margin:0;padding:0}
html,body{width:1200px;height:4816px;overflow:hidden;background:var(--paper)}
body{font-family:"Roboto",Arial,sans-serif;color:var(--ink);position:relative}
.abs{position:absolute}
.heading{font-family:"Roboto Condensed","Arial Narrow",sans-serif;font-weight:700;color:var(--blue)}
.btn{display:inline-block;font-family:"Roboto",Arial,sans-serif;font-weight:700;font-size:14px;letter-spacing:.5px;padding:12px 16px;border:2px solid var(--navy);text-transform:uppercase;line-height:1}
.btn-fill{background:var(--navy);color:#fff}
.btn-line{background:#fff;color:var(--navy)}
.btn-ghost{background:transparent;color:#fff;border-color:#fff}

/* header */
.topbar{left:0;top:0;width:1200px;height:104px;background:#fff}
.brand{left:112px;top:34px;display:flex;align-items:center;gap:12px}
.brand-mark{width:26px;height:26px;border-radius:50%;background:var(--navy)}
.brand-name{font-family:"Roboto",sans-serif;font-weight:500;font-size:28px;color:var(--navy);line-height:1}
.search{left:622px;top:30px;display:flex;height:40px;border:1px solid var(--line)}
.search-field{width:130px;padding:0 12px;font-size:14px;color:var(--muted);display:flex;align-items:center;border-right:1px solid var(--line)}
.search-loc{width:190px;justify-content:space-between}
.search-btn{background:var(--blue);color:#fff;font-weight:700;font-size:14px;padding:0 14px;display:flex;align-items:center}
.nav{left:0;top:104px;width:1200px;height:56px;background:var(--navy-deep);display:flex;justify-content:space-between;padding:0 112px;align-items:center}
.nav a{color:#fff;font-size:16px;font-weight:500;text-decoration:none;width:150px;text-align:center;height:56px;line-height:56px}
.nav a.active{background:var(--blue)}

/* hero */
.hero{left:0;top:160px;width:1200px;height:600px;overflow:hidden}
.hero-photo{position:absolute;inset:0;background:linear-gradient(100deg,#c9cdd3 0%,#e6e7ea 40%,#b9bec6 70%,#8a8f98 100%)}
.hero svg{position:absolute;left:0;top:0}
.hero-title{left:112px;top:90px;width:480px;font-family:"Roboto",sans-serif;font-weight:700;font-size:50px;color:#fff;line-height:1.15}
.hero-sub{left:112px;top:250px;width:400px;font-size:30px;color:var(--sky);line-height:1.3}
.hero-ctas{left:112px;top:390px;display:flex;gap:14px}

/* intro */
.intro{left:150px;top:860px;width:900px;text-align:center;font-size:18px;line-height:1.6;color:#4a4a4a}

/* split blocks */
.split-title{font-size:54px;line-height:1}
.swoosh{display:block;margin-top:4px}
.split-copy{font-size:18px;line-height:1.55;color:#444}
.split-ctas{display:flex;gap:14px}

/* testimonials */
.testis{left:0;top:2240px;width:1200px;height:580px;background:linear-gradient(180deg,#e9ebee,#dfe2e6 60%,#e9ebee)}
.testis-title{left:0;top:2300px;width:1200px;text-align:center;font-size:54px}
.quote-card{left:112px;top:2484px;width:976px;height:250px;background:#fff;border:1px solid var(--line);text-align:center;padding:70px 70px 0}
.quote-badge{left:570px;top:2440px}
.quote-text{font-size:17px;font-style:italic;line-height:1.6;color:#333}
.quote-name{margin-top:14px;color:var(--blue);font-size:17px}
.quote-role{font-size:16px;color:#333;margin-top:4px}

/* blog */
.blog-title{left:0;top:2878px;width:1200px;text-align:center;font-size:54px}
.post{width:468px;height:640px;border:1px solid var(--line);background:#fff;padding:16px;text-align:center}
.post-img{width:434px;height:206px}
.post h3{font-family:"Roboto",sans-serif;font-weight:500;font-size:26px;color:#222;margin-top:20px;line-height:1.3}
.post-meta{font-size:15px;color:#555;margin-top:8px}
.post p{font-size:15px;color:#444;line-height:1.5;margin-top:12px;padding:0 10px}
.post .btn{margin-top:20px}

/* cta band */
.cta-band{left:0;top:3820px;width:1200px;height:560px;background:linear-gradient(120deg,#1c3b5e,#0f2b4b 45%,#263f5e)}
.cta-card{width:476px;height:384px;background:#fff;text-align:center;padding-top:44px}
.cta-card h3{font-family:"Roboto",sans-serif;font-weight:500;font-size:32px;color:var(--blue);line-height:1.2;margin-top:26px}
.cta-card .btn{margin-top:24px}

/* footer */
.foot-col h4{font-family:"Roboto Condensed",sans-serif;font-weight:700;font-size:28px;color:var(--blue)}
.foot-col p{font-size:15px;line-height:1.45;color:#444;margin-top:14px;width:230px}
.foot-col .btn{margin-top:18px}
.addr-card{margin-top:14px;width:290px;background:#fff;border:1px solid var(--line);display:flex;gap:14px;padding:14px}
.addr-mark{width:60px;height:60px;background:var(--blue);flex:none}
.addr-card div{font-size:14px;line-height:1.45;color:#333}
.copyright{left:0;top:4762px;width:1200px;height:54px;border-top:1px solid var(--line);text-align:center;line-height:54px;font-size:15px;color:#333}
</style>
</head>
<body>

<header>
  <div class="abs topbar"></div>
  <div class="abs brand"><span class="brand-mark"></span><span class="brand-name">Northgate Talent</span></div>
  <div class="abs search">
    <div class="search-field">Search Here</div>
    <div class="search-field search-loc">Location
      <svg width="12" height="16" viewBox="0 0 12 16"><path d="M6 0a6 6 0 0 0-6 6c0 4.5 6 10 6 10s6-5.5 6-10a6 6 0 0 0-6-6zm0 8.5A2.5 2.5 0 1 1 6 3.5a2.5 2.5 0 0 1 0 5z" fill="#555"/></svg>
    </div>
    <div class="search-btn">SEARCH JOBS</div>
  </div>
  <nav class="abs nav">
    <a class="active">HOME</a><a>ABOUT US</a><a>JOB SEEKERS</a><a>CLIENTS</a><a>CONTACT US</a>
  </nav>
</header>

<section class="abs hero">
  <div class="hero-photo" role="img" aria-label="Photo of smiling professionals seated in a row waiting for job interviews"></div>
  <svg width="1200" height="600" viewBox="0 0 1200 600">
    <defs><linearGradient id="heroBlue" x1="0" y1="0" x2="1" y2="1"><stop offset="0" stop-color="#1e72c0"/><stop offset="1" stop-color="#0b3c70"/></linearGradient></defs>
    <path d="M0 0H700C760 120 720 330 560 480C450 580 250 600 0 600Z" fill="url(#heroBlue)"/>
    <path d="M700 0C760 120 720 330 560 480C450 580 250 600 0 600" fill="none" stroke="#fff" stroke-width="10"/>
  </svg>
  <h1 class="abs hero-title">The Right People For The Right Jobs!</h1>
  <p class="abs hero-sub">Bridging the talent gap in Technical Staffing</p>
  <div class="abs hero-ctas"><span class="btn btn-ghost">Hire Talent</span><span class="btn btn-ghost">Get Hired</span></div>
</section>

<p class="abs intro">Northgate Talent is a National Technical Staffing and Recruiting Solutions Provider founded in 2013 focused on matching contract and full time Engineering and IT professionals with new and exciting employment opportunities!</p>

<section>
  <svg class="abs" style="left:620px;top:1072px" width="580" height="528" viewBox="0 0 580 528" role="img" aria-label="Photo of a smiling job candidate in a suit holding his resume">
    <defs><linearGradient id="simplyPhoto" x1="0" y1="0" x2="1" y2="0"><stop offset="0" stop-color="#c7c3bd"/><stop offset=".5" stop-color="#a49f99"/><stop offset="1" stop-color="#d8d6d2"/></linearGradient></defs>
    <path d="M120 0H580V528H0C110 420 140 260 80 120C65 80 85 30 120 0Z" fill="url(#simplyPhoto)"/>
    <path d="M120 0C85 30 65 80 80 120C140 260 110 420 0 528" fill="none" stroke="#1762a8" stroke-width="8"/>
  </svg>
  <div class="abs" style="left:112px;top:1108px">
    <h2 class="heading split-title">Simply Said...</h2>
    <svg class="swoosh" width="200" height="16" viewBox="0 0 200 16"><path d="M100 14C140 6 175 3 200 2C170 9 140 12 100 14Z" fill="#1762a8"/></svg>
  </div>
  <p class="abs split-copy" style="left:112px;top:1184px;width:470px">Simply said… WE LOVE TO RECRUIT! It's our passion and we take it very seriously! It is not easy for JOB SEEKERS to put their job search efforts and trust in the hands of someone else, especially when there are so many Staffing Firms to choose from. So how do you know you are choosing the best Staffing Representation possible?</p>
  <div class="abs split-ctas" style="left:112px;top:1472px"><span class="btn btn-fill">Learn More</span><span class="btn btn-line">View Jobs</span></div>
</section>

<section>
  <svg class="abs" style="left:0;top:1668px" width="600" height="512" viewBox="0 0 600 512" role="img" aria-label="Photo of a young woman smiling among candidates seated for interviews">
    <defs><linearGradient id="respPhoto" x1="0" y1="0" x2="1" y2="1"><stop offset="0" stop-color="#d6d3cf"/><stop offset=".6" stop-color="#9b948e"/><stop offset="1" stop-color="#c3beb8"/></linearGradient></defs>
    <path d="M0 0H520C590 120 600 300 560 400C530 470 500 500 470 512H0Z" fill="url(#respPhoto)"/>
    <path d="M520 0C590 120 600 300 560 400C530 470 500 500 470 512" fill="none" stroke="#1762a8" stroke-width="8"/>
  </svg>
  <div class="abs" style="left:620px;top:1696px">
    <h2 class="heading split-title">Are You Responsible</h2>
    <svg class="swoosh" style="margin-left:260px" width="200" height="16" viewBox="0 0 200 16"><path d="M100 14C140 6 175 3 200 2C170 9 140 12 100 14Z" fill="#1762a8"/></svg>
  </div>
  <p class="abs split-copy" style="left:620px;top:1774px;width:470px">for Technical Staffing within your organization? Are you satisfied with your current Supplier(s)' overall performance? Does it appear they identify potential Candidate(s) based purely on "buzz-word" searches? Is it evident they just do not grasp the scope and responsibilities of your technical staffing need(s)?</p>
  <div class="abs split-ctas" style="left:620px;top:2040px"><span class="btn btn-fill">Learn More</span><span class="btn btn-line">Hire Talent</span></div>
</section>

<section>
  <div class="abs testis" role="img" aria-label="Faded photo of a team meeting around a table"></div>
  <h2 class="abs heading testis-title">Our Testimonials
    <svg class="swoosh" style="margin:2px auto 0 auto;position:relative;left:110px" width="200" height="16" viewBox="0 0 200 16"><path d="M100 14C140 6 175 3 200 2C170 9 140 12 100 14Z" fill="#1762a8"/></svg>
  </h2>
  <div class="abs quote-card">
    <p class="quote-text">"Dan Miller is an excellent recruiter. He is articulate, honest, has a good nature and is an effective information conduit between his clients and candidates. He gave me the feeling he is there for the big picture desiring to forge a future relationship that will be mutually beneficial to both of us."</p>
    <p class="quote-name">Sam R.</p>
    <p class="quote-role">- Electrical Test Engineer in the Automotive Sector</p>
  </div>
  <svg class="abs quote-badge" width="60" height="80" viewBox="0 0 60 80">
    <rect x="10" y="0" width="40" height="80" fill="#fff"/>
    <circle cx="30" cy="40" r="30" fill="#0b2f55"/>
    <path d="M22 28h6l-4 24h-6zM36 28h6l-4 24h-6z" fill="#fff"/>
  </svg>
</section>

<section>
  <h2 class="abs heading blog-title">Our Latest Blog
    <svg class="swoosh" style="margin:2px auto 0 auto;position:relative;left:90px" width="200" height="16" viewBox="0 0 200 16"><path d="M100 14C140 6 175 3 200 2C170 9 140 12 100 14Z" fill="#1762a8"/></svg>
  </h2>
  <article class="abs post" style="left:120px;top:3100px">
    <div class="post-img" role="img" aria-label="Photo of a woman working on a laptop at a desk" style="background:linear-gradient(135deg,#8a7a6c,#d2c7bb 55%,#5e564f)"></div>
    <h3>Ways To Make The Most Of The Hot Jobs Market</h3>
    <p class="post-meta">June 17, 2019 by northgate</p>
    <p>"This is the tightest labor market we have seen in years. Unemployment sits at a low point and wage growth keeps climbing, so skilled candidates now hold real leverage in every hiring conversation across the country.</p>
    <span class="btn btn-line">Hire Talent</span>
  </article>
  <article class="abs post" style="left:620px;top:3100px">
    <div class="post-img" role="img" aria-label="Photo of two business people shaking hands" style="background:linear-gradient(135deg,#c7d3df,#eef2f6 50%,#3d5470)"></div>
    <h3>Back To Basics: Meeting Employees' Needs To Improve</h3>
    <p class="post-meta">June 6, 2019 by northgate</p>
    <p>The benefits of employee satisfaction are well established, so HR pros and leaders across all industries spend a great deal of time focused on maintaining those benefits for their teams. There is no shortage of approaches.</p>
    <span class="btn btn-line">Hire Talent</span>
  </article>
</section>

<section>
  <div class="abs cta-band" role="img" aria-label="Darkened photo of job candidates waiting in an office"></div>
  <div class="abs cta-card" style="left:112px;top:3920px">
    <svg width="64" height="60" viewBox="0 0 64 60" fill="none" stroke="#0b2f55" stroke-width="2.5">
      <circle cx="32" cy="18" r="10"/><path d="M14 50c0-11 8-18 18-18s18 7 18 18"/><rect x="8" y="50" width="48" height="6"/>
    </svg>
    <h3>Looking For Career Minded<br>Candidates?</h3>
    <span class="btn btn-fill">Request Talent</span>
  </div>
  <div class="abs cta-card" style="left:612px;top:3920px">
    <svg width="64" height="60" viewBox="0 0 64 60" fill="none" stroke="#0b2f55" stroke-width="2.5">
      <circle cx="28" cy="24" r="16"/><path d="M40 36l16 16"/><circle cx="28" cy="20" r="5"/><path d="M19 34c2-5 5-7 9-7s7 2 9 7"/>
    </svg>
    <h3>Looking For Career<br>Opportunities?</h3>
    <span class="btn btn-fill">Request Talent</span>
  </div>
</section>

<footer>
  <div class="abs foot-col" style="left:112px;top:4426px">
    <h4>GET HIRED</h4>
    <p>Nam libero tempore, cum soluta nobis est eligendi optio cumque nihil impedit quo minus id quod.</p>
    <span class="btn btn-fill">Search Now</span>
  </div>
  <div class="abs foot-col" style="left:424px;top:4426px">
    <h4>HIRE TALENT</h4>
    <p>Nam libero tempore, cum soluta nobis est eligendi optio cumque nihil impedit quo minus id quod.</p>
    <span class="btn btn-fill">Start Today</span>
  </div>
  <div class="abs foot-col" style="left:784px;top:4426px">
    <h4>Address</h4>
    <div class="addr-card">
      <span class="addr-mark"></span>
      <div>Northgate Talent, Inc.<br>48 Harbor Street, Suite 2<br>Millbrook, MA 01999</div>
    </div>
  </div>
  <div class="abs copyright">Copyright © 2020 Northgate Talent. All Rights Reserved.</div>
</footer>

</body>
</html>
```